Harbourlight Dental Centre Kelvale business cards and presentation folder

dental practice needing innovative black business cards for 2 different dentists witrh appointment details written at the back of the card for the patient.
name of dentists: Dr Anjali R Venkatesan B.D.S., M.P.H (Melb)
Dr. Raj Kalpat B.D.S.

Target Market(s)

professioinal, working class

Industry/Entity Type

Dental Clinic

Contact Information for Business Card

Dr. Raj Kalpat B.D.S.

Font styles to use
Sans Serif

Requirements
Must have
• Front side: logo
• dentist name
• phone number: 07- 5918 2243
• back side: appointment details: date, time,
• Address: 117C, 58 Tarrow Street, Kelvale - 4561, Queensland
• Email: admin@harbourlightdentalkelvale.example.au
• Website: www.harbourlightdental.example.au
• preferable logo colors
Nice to have
• classy look more pleasing

```html
<!DOCTYPE html>
<html lang="en">
<head>
<meta charset="utf-8">
<title>Harbourlight Dental Centre Kelvale – Business Card</title>
<link rel="stylesheet" href="https://fonts.googleapis.com/css2?family=PT+Sans:wght@400;700&family=PT+Sans+Narrow:wght@700&display=swap">
<style>
  :root {
    --backdrop: #e9e7e3;
    --card-black: #231f20;
    --sage: #a9c78b;
    --sage-text: #a9c78b;
    --silver: #a7a9ac;
    --ink: #2b2b2b;
    --paper-text: #e6e6e6;
  }
  * { margin: 0; padding: 0; box-sizing: border-box; }
  html, body { width: 1200px; height: 987px; overflow: hidden; }
  body {
    background: var(--backdrop);
    font-family: "PT Sans", Arial, sans-serif;
    position: relative;
  }
  .card {
    position: absolute;
    left: 293px;
    width: 615px;
    height: 349px;
    border-radius: 20px;
    overflow: hidden;
    background: var(--card-black);
    box-shadow: 0 4px 14px rgba(0,0,0,0.25);
  }
  .card--front { top: 131px; }
  .card--back { top: 506px; }
  .front-shapes { position: absolute; inset: 0; }

  .dentists { position: absolute; left: 23px; top: 32px; color: var(--ink); }
  .dentist-name {
    font-family: "PT Sans Narrow", "Arial Narrow", sans-serif;
    font-weight: 700;
    font-size: 21px;
    line-height: 24px;
  }
  .dentist-degree {
    font-family: "PT Sans Narrow", "Arial Narrow", sans-serif;
    font-weight: 700;
    font-size: 15px;
    line-height: 17px;
  }
  .dentist-degree--inline { font-size: 15px; }

  .address {
    position: absolute; left: 23px; top: 173px;
    font-size: 16px; line-height: 22px; color: var(--ink);
    font-style: normal;
  }
  .contacts {
    position: absolute; left: 23px; top: 252px;
    list-style: none; font-size: 15px; color: var(--ink);
  }
  .contacts li { display: flex; align-items: center; height: 23px; }
  .contacts svg { width: 15px; height: 15px; margin-right: 9px; flex: none; }
  .contacts .phone { margin-right: 14px; }

  .brand-name {
    position: absolute;
    color: var(--sage-text);
    font-weight: 400;
    text-transform: uppercase;
    letter-spacing: 1px;
    text-align: center;
    line-height: 1.15;
  }
  .brand-name--front { left: 330px; top: 42px; width: 270px; font-size: 23px; }
  .brand-name--back { left: 107px; top: 58px; width: 400px; font-size: 33px; }

  .appointment-title {
    position: absolute; left: 0; right: 0; top: 198px;
    text-align: center; color: var(--sage-text);
    font-weight: 700; font-size: 21px; letter-spacing: 0.3px;
  }
  .appointment-row {
    position: absolute; left: 31px; right: 32px;
    display: flex; align-items: baseline;
    color: var(--paper-text); font-size: 16px;
  }
  .appointment-row--name { top: 246px; }
  .appointment-row--when { top: 292px; }
  .fill-line {
    flex: 1; border-bottom: 2px dotted #8c8c8c;
    margin: 0 2px; transform: translateY(-4px);
  }
  .fill-line--date { flex: 1.05; }
  .fill-line--time { flex: 0.9; }
</style>
</head>
<body>

<section class="card card--front" aria-label="Business card front">
  <svg class="front-shapes" viewBox="0 0 615 349" preserveAspectRatio="none" aria-hidden="true">
    <rect width="615" height="349" fill="var(--card-black)"/>
    <path d="M246 0 H292 C300 150 390 275 504 349 C350 270 262 130 246 0 Z" fill="var(--silver)"/>
    <path d="M0 0 H246 C262 130 350 270 504 349 H0 Z" fill="var(--sage)"/>
  </svg>

  <div class="dentists">
    <p class="dentist-name">Dr Anjali R Venkatesan</p>
    <p class="dentist-degree">B.D.S., M.P.H (Melb)</p>
    <p class="dentist-name">Dr. Raj Kalpat <span class="dentist-degree dentist-degree--inline">B.D.S.</span></p>
  </div>

  <address class="address">
    117C, 58 Tarrow Street<br>
    Kelvale - 4561<br>
    Queensland
  </address>

  <ul class="contacts">
    <li>
      <svg class="phone" viewBox="0 0 24 24" aria-hidden="true"><path fill="var(--ink)" d="M6.6 10.8c1.4 2.8 3.8 5.1 6.6 6.6l2.2-2.2c.3-.3.7-.4 1-.2 1.1.4 2.3.6 3.6.6.6 0 1 .4 1 1V20c0 .6-.4 1-1 1C10.6 21 3 13.4 3 4c0-.6.4-1 1-1h3.5c.6 0 1 .4 1 1 0 1.3.2 2.5.6 3.6.1.3 0 .7-.2 1l-2.3 2.2z"/></svg>
      07- 5918 2243
    </li>
    <li>
      <svg viewBox="0 0 24 24" aria-hidden="true"><path fill="var(--ink)" d="M2 5h20v14H2z"/><path d="M2 5l10 8 10-8" fill="none" stroke="var(--sage)" stroke-width="2"/></svg>
      admin@harbourlightdentalkelvale.example.au
    </li>
    <li>
      <svg viewBox="0 0 24 24" aria-hidden="true"><circle cx="12" cy="12" r="10" fill="var(--ink)"/><path d="M2 12h20M12 2c3 3 3 17 0 20M12 2c-3 3-3 17 0 20" fill="none" stroke="var(--sage)" stroke-width="1.5"/></svg>
      www.harbourlightdental.example.au
    </li>
  </ul>

  <p class="brand-name brand-name--front">Harbourlight Dental Centre Kelvale</p>
</section>

<section class="card card--back" aria-label="Business card back">
  <p class="brand-name brand-name--back">Harbourlight Dental Centre Kelvale</p>

  <h2 class="appointment-title">NEXT APPOINTMENT</h2>

  <div class="appointment-row appointment-row--name">
    <span>Name :</span><span class="fill-line"></span>
  </div>
  <div class="appointment-row appointment-row--when">
    <span>Date :</span><span class="fill-line fill-line--date"></span>
    <span>Time :</span><span class="fill-line fill-line--time"></span>
    <span>AM/BM</span>
  </div>
</section>

</body>
</html>
```